Local Chiropractoc needs Modern Website

This website needs to have an upscale look with a very modern feel.

This is for a home page psd layout and an interior page psd file so 2 files total

Below is the information and websites to reference

Add Logo that is attached.

Build a color scheme similar to this website image titled "chiro-1" using the golds, whites, blacks and browns from the color of the logo

I want to see a light background so it makes the images and logo stick out

Must Include these pages in a horizontal menu bar in this order:
Home, Why Bright Harbor?, How Chiropractic Helps, Ask the Doctor, Work Place Wellness, Request an Appointment, Blog, Contact Us

Please add the following social media logos to the top and footer of the website: Chatterloop, Vennly+, Clipstream

Build a "classy looking" Make An Appointment Button into the header with the contact info below

Phone Number:
555-014-2736

Address:
4821 North Marrow Blvd, Suite #7
Lakeland, FL 39207

This website needs 4 rotating banners. Please reference a layout similar to this for the banners: http://fernvalespine.example/. However design it nicer than this website

Below are the description for each banner

Rotating Banner #1
Use Image: Patients are Saying
Add a line of text: "What our Patients are Saying"

Rotating Banner #2
Use Image: Becoming a Patient
Add a line of text: "Interested in Becoming a Patient"

Rotating Banner #3
Use Image: Dinner with Doctor
Add a line of text: "Win A free Dinner with Dr. Quillon"

Rotating Banner #4
Use Image: Chatterloop
Add a line of text: Follow us on Chatterloop
Bullet point these 4 lines underneath the "Follow us on Chatterloop" text:
- Cutting Edge Health News
- Healthy Recipes
- Newest Health Products
- Clinic Events

I'd like to see a free consultation box similar to the "chiro-1" image. Fields to include are: First Name, Last Name, Phone Number, Comments

For the body, please fill it with latin text. Please design a professional 2 column layout similar to the www.fernvalespine.example website. (DO NOT COPY THIS WEBSITE, USE IT AS REFERENCE)

In the left column include in this order:
Video
Rate us on Vennly Button, Find us on Chatterloop Button
Welcome Letter

In the right column include this:

Office Hours
Monday: 8:00-11:00, 2:00-5:00
Tuesday: 8:30-11:00, 2:00-5:30
Wednesday: 8:00-11:00, 2:00-5:00
Thursday: 10:00-12:00, 2:30-5:00
Friday: 8:00-10:00, 1:00-5:00
Saturday: Closed
Sunday: Closed

Patient Testimonials
Fill with a latin text testimonial. This spot will rotate different testimonials

For the footer please design something similar to the layout of this: http://www.tidewellspinecare.example/

Also include in the Footer: Powered by Ostrel Pixel Works

```html
<!DOCTYPE html>
<html lang="en">
<head>
<meta charset="utf-8">
<title>Bright Harbor Chiropractic</title>
<link href="https://fonts.googleapis.com/css2?family=Source+Sans+3:wght@300;400;600;700&display=swap" rel="stylesheet">
<style>
:root{
  --gold:#b89a62;
  --teal:#0d4a60;
  --teal-dark:#06445e;
  --ink:#1b1b1b;
  --text:#555;
  --muted:#777;
  --line:#dcdcdc;
  --panel:#f3f3f3;
  --icon:#9a9a9a;
  --alert:#e3141b;
}
*{box-sizing:border-box;margin:0;padding:0}
html,body{width:1200px;height:1000px;overflow:hidden;background:#fff}
body{font-family:"Source Sans 3",sans-serif;color:var(--text);position:relative}
.abs{position:absolute}

.brand{left:121px;top:36px;width:150px;color:var(--ink);font-weight:700;font-size:25px;line-height:26px;letter-spacing:.5px;text-transform:uppercase}
.brand small{display:block;font-size:14px;line-height:18px;letter-spacing:1px;margin-top:4px}
.brand-mark{display:inline-block;width:10px;height:10px;background:var(--gold);margin-right:6px;vertical-align:middle}

.appt-btn{left:311px;top:28px;width:155px;height:40px;background:var(--gold);color:#fff;font-size:13px;display:flex;align-items:center;justify-content:center}
.phone{left:501px;top:20px;font-size:24px;font-weight:600;color:var(--gold)}
.address{left:501px;top:51px;font-size:16px;color:var(--ink);white-space:nowrap}
.follow{left:883px;top:51px;font-size:16px;font-weight:300;color:var(--muted)}
.social{left:962px;top:48px;display:flex;gap:11px}
.social span{width:24px;height:24px;border-radius:50%;background:var(--icon)}

.main-nav{left:311px;top:106px;width:745px;display:flex;justify-content:space-between;font-size:16px;font-weight:300;color:var(--muted);white-space:nowrap}
.main-nav .dot{width:5px;height:5px;border-radius:50%;background:var(--ink);align-self:center}

.hero-photo{left:119px;top:146px;width:628px;height:416px;background:linear-gradient(135deg,#4f7a2e 0%,#a7a05a 35%,#e6c9a9 60%,#d9b39a 100%)}
.hero-panel{left:747px;top:146px;width:309px;height:416px;background:var(--panel);text-align:center}
.hero-title{position:absolute;left:0;right:14px;top:60px;font-weight:300;font-size:30px;line-height:38px;color:var(--text);text-transform:uppercase}
.hero-title b{display:block;font-weight:600;font-size:34px;color:#000;line-height:40px}
.hero-title .big{display:block;font-weight:600;font-size:44px;color:var(--teal);line-height:64px}
.hero-btn{left:101px;top:282px;width:110px;height:35px;border:1px solid #999;background:#fff;color:var(--ink);font-size:16px;font-weight:300;display:flex;align-items:center;justify-content:center}

.tab{top:521px;height:41px;font-size:16px;display:flex;align-items:center;justify-content:center;white-space:nowrap}
.tab-consult{left:161px;width:150px;background:#fff;color:var(--ink)}
.tab-call{left:316px;width:112px;background:var(--teal-dark);color:#fff}

.field{height:45px;border:1px solid var(--line);background:#fff;color:#888;font-size:16px;font-weight:300;padding-left:14px;display:flex;align-items:center}
.submit{left:866px;top:668px;width:150px;height:45px;background:var(--teal-dark);color:#fff;font-size:16px;display:flex;align-items:center;justify-content:center}

.video{left:121px;top:766px;width:565px;height:234px;background:linear-gradient(90deg,#6d5450 0%,#8a7068 40%,#a99e9a 70%,#6b5654 100%)}
.video-label{left:0;top:0;height:30px;display:flex;font-size:14px;color:#fff;white-space:nowrap}
.video-label .flag{width:30px;background:var(--alert);display:flex;align-items:center;justify-content:center}
.video-label .name{background:#1a1716;padding:0 12px;display:flex;align-items:center}
.play{left:250px;top:175px;width:46px;height:46px;border-radius:50%;background:#1a1a1a;border:2px solid #fff}
.play::after{content:"";position:absolute;left:17px;top:13px;border-left:13px solid #fff;border-top:8px solid transparent;border-bottom:8px solid transparent}

.hours{left:747px;top:765px;width:308px;height:260px;border:1px solid var(--line);overflow:hidden}
.hours-corner{position:absolute;right:-1px;top:-1px}
.hours h2{position:absolute;left:21px;top:22px;font-size:25px;font-weight:400;color:var(--teal)}
.hours-list{position:absolute;left:20px;top:72px;width:266px;list-style:none}
.hours-list li{height:40px;border-bottom:1px solid var(--line);display:flex;justify-content:space-between;align-items:center;font-size:16px;white-space:nowrap}
.hours-list .day{color:var(--muted);font-weight:300}
.hours-list .time{color:#333;font-weight:600}
</style>
</head>
<body>
<header>
  <div class="abs brand"><span class="brand-mark"></span>Bright Harbor<small>Chiropractic</small></div>
  <div class="abs appt-btn">Make an Appointment</div>
  <div class="abs phone">555-014-2736</div>
  <div class="abs address">4821 North Marrow Blvd, Suite #7 Lakeland, FL 39207</div>
  <div class="abs follow">Folow Us:</div>
  <div class="abs social" aria-label="Chatterloop, Clipstream, Vennly+"><span></span><span></span><span></span></div>
  <nav class="abs main-nav">
    <span>Home</span><i class="dot"></i><span>Why Bright Harbor?</span><i class="dot"></i><span>How Chiropractic Helps</span><i class="dot"></i><span>Ask the Doctor</span><i class="dot"></i><span>Work Place Wellness</span><i class="dot"></i><span>Blog</span><i class="dot"></i><span>Contact Us</span>
  </nav>
</header>

<section>
  <div class="abs hero-photo" role="img" aria-label="Smiling family of four posing together outdoors"></div>
  <div class="abs hero-panel">
    <div class="hero-title">What our<b>Patients</b>are<span class="big">Saying</span></div>
    <div class="abs hero-btn">Click Here</div>
  </div>
  <div class="abs tab tab-consult">Free Consultation</div>
  <div class="abs tab tab-call">Call Us Now</div>
</section>

<form>
  <div class="abs field" style="left:164px;top:611px;width:359px">First Name</div>
  <div class="abs field" style="left:164px;top:668px;width:359px">Last Name</div>
  <div class="abs field" style="left:560px;top:611px;width:455px;padding-left:18px">Comments</div>
  <div class="abs field" style="left:560px;top:668px;width:270px;padding-left:17px">Phone Number</div>
  <div class="abs submit">Submit</div>
</form>

<main>
  <div class="abs video" role="img" aria-label="Video still of a chiropractor with a patient in the clinic">
    <div class="abs video-label">
      <span class="flag"><svg width="16" height="11" viewBox="0 0 16 11"><rect x="0" y="1" width="10" height="9" rx="1" fill="#fff"/><polygon points="10,5.5 16,1 16,10" fill="#fff"/></svg></span>
      <span class="name">Bright Harbor Chiropractic</span>
    </div>
    <div class="abs play"></div>
  </div>

  <aside class="abs hours">
    <svg class="hours-corner" width="34" height="33" viewBox="0 0 34 33"><polygon points="0,0 34,0 34,33" fill="#0d4a60"/></svg>
    <h2>Office Hours:</h2>
    <ul class="hours-list">
      <li><span class="day">Monday:</span><span class="time">8:00-11:00, 2:00-5:00</span></li>
      <li><span class="day">Tuesday:</span><span class="time">8:30-11:00, 2:00-5:30</span></li>
      <li><span class="day">Wednesday:</span><span class="time">8:00-11:00, 2:00-5:00</span></li>
      <li><span class="day">Thursday:</span><span class="time">10:00-12:00, 2:30-5:00</span></li>
    </ul>
  </aside>
</main>
</body>
</html>
```